QBoost480 Business Card Design

I am in need of a business card design.

Business Name: Quantum Boost 480 or Qboost480 (we can try the business card with both variations)

I would like it to be somewhat different from the "average" business card

What do we do?

We link up with distributors of different items and we Market their products, sell their products, fulfill the shipment, and handle all customer service that goes along with it.

I will be uploading our logo as well as other business card ideas that i have seen and liked on the web.

I like the style of the "graphic design" business card that i uploaded. I was thinking maybe something like that but instead would read.

SYNC | SELL | SHIP

With maybe:
a computer or a Sync icon underneath SYNC
Some form of money sign underneath Sell
a delivery truck or something underneath SHIP.

And then I was thinking maybe put the logo on the back side like in the other business card that i uploaded.

I definitely want a double sided business card.

These are only my suggestions and if i was very confident in my idea then I wouldn't have to be on here. (So make what you think is nice because my opinion is probably not so great anyway!!)

Everything can be changed.

ALSO, For the logo
We can try and remove the text multi channel selling

For the Business card contact info:
Milo Quenton
CEO
2914 Ravensby Street
J7T-2K8
Montreal, Quebec

Thanks

Target Market(s)

Businesses

Industry/Entity Type

Information Technology

Font styles to use
Serif
Sans Serif
Decorative

Colors
34a6d6
33b8a4
aaaaaa
85cae6
33a6d7
0492cd
9d9d9d

Requirements
Must have
• Double Sided Business card
Nice to have
• Illustration graphics / Icons underneath the main points

```html
<!DOCTYPE html>
<html lang="en">
<head>
<meta charset="utf-8">
<title>QBoost480 Business Card</title>
<link href="https://fonts.googleapis.com/css2?family=Arimo:wght@400;700&family=Exo+2:ital,wght@1,700&display=swap" rel="stylesheet">
<style>
  :root {
    --mint: #4df98b;
    --lime: #7ef500;
    --sky: #4fd4fa;
    --slate: #7d8487;
    --paper: #ffffff;
    --backdrop: #e4e6e8;
  }
  html, body {
    margin: 0;
    width: 1200px;
    height: 1200px;
    overflow: hidden;
    background: var(--backdrop);
  }
  .sheet {
    position: relative;
    width: 1200px;
    height: 1200px;
  }
  .card {
    position: absolute;
    left: 100px;
    width: 1000px;
    height: 571px;
    background: var(--paper);
    box-shadow: 0 6px 18px rgba(0,0,0,0.25);
  }
  .card--front { top: 25px; }
  .card--back { top: 614px; }
  .card svg { display: block; width: 100%; height: 100%; }
  .text { font-family: "Arimo", Arial, sans-serif; fill: var(--paper); }
  .name { font-size: 31px; }
  .role { font-size: 22px; }
  .contact { font-size: 24px; }
  .brand { font-family: "Arimo", Arial, sans-serif; font-weight: 700; font-size: 62px; fill: var(--sky); }
  .pillar { font-family: "Arimo", Arial, sans-serif; font-weight: 700; font-size: 21px; fill: var(--lime); }
  .tagline { font-family: "Exo 2", "Arial Black", sans-serif; font-style: italic; font-weight: 700; font-size: 30px; fill: var(--slate); letter-spacing: 2px; }
</style>
</head>
<body>
<main class="sheet">

  <section class="card card--front" aria-label="Card front">
    <svg viewBox="0 0 1050 600" xmlns="http://www.w3.org/2000/svg">
      <!-- sweeping curves -->
      <path class="sweep-green" fill="var(--lime)" d="M155,0 Q760,110 1012,585 Q760,170 360,0 Z"/>
      <path class="sweep-blue" fill="var(--sky)" d="M330,0 Q780,120 1012,585 Q820,190 600,0 Z"/>
      <path class="edge-blue" fill="var(--sky)" d="M990,0 L1050,0 L1050,130 Q1012,320 1012,585 Q960,300 990,0 Z"/>
      <path class="edge-green" fill="var(--lime)" d="M1050,140 L1050,563 L1030,563 Q1030,320 1050,140 Z"/>

      <!-- top band -->
      <rect class="band-blue" fill="var(--sky)" x="0" y="197" width="83" height="24"/>
      <path class="band-blue" fill="var(--sky)" d="M262,197 L612,197 L652,221 L262,221 Z"/>
      <path class="band-wedge" fill="var(--slate)" d="M92,197 L252,197 L120,221 L92,221 Z"/>
      <path class="band-wedge" fill="var(--lime)" d="M252,200 L252,221 L130,221 Z"/>

      <!-- main panel -->
      <path class="panel" fill="var(--mint)" d="M0,230 L668,230 L985,563 L0,563 Z"/>
      <rect class="divider" fill="var(--paper)" x="0" y="340" width="812" height="3"/>

      <!-- bottom band -->
      <path class="band-lime" fill="var(--lime)" d="M0,526 L492,526 L526,563 L0,563 Z"/>
      <path class="band-slate" fill="var(--slate)" d="M500,526 L526,526 L560,563 L534,563 Z"/>
      <rect fill="var(--paper)" x="0" y="520" width="530" height="5"/>

      <!-- identity -->
      <text class="text name" x="92" y="300">Milo Quenton</text>
      <text class="text role" x="92" y="330">CEO</text>

      <!-- phone -->
      <path fill="var(--paper)" d="M93,386 Q101,378 109,386 L107,390 L104,389 L103,386 Q101,385 99,386 L98,389 L95,390 Z M96,391 L106,391 L108,398 L94,398 Z"/>
      <text class="text contact" x="118" y="398">418-260395</text>
      <!-- mobile -->
      <rect x="96" y="409" width="11" height="21" rx="2" fill="none" stroke="var(--paper)" stroke-width="1.5"/>
      <text class="text contact" x="118" y="430">+5147302618</text>
      <!-- mail -->
      <rect x="93" y="448" width="17" height="12" fill="none" stroke="var(--paper)" stroke-width="1.6"/>
      <path d="M93,448 L101.5,455 L110,448 M93,460 L99,454 M110,460 L104,454" fill="none" stroke="var(--paper)" stroke-width="1.4"/>
      <text class="text contact" x="118" y="462">miloquenton_qboost480@mailbox.com</text>

      <!-- web -->
      <circle cx="535" cy="389" r="8" fill="none" stroke="var(--paper)" stroke-width="1.6"/>
      <path d="M527,389 L543,389 M535,381 Q530,389 535,397 Q540,389 535,381" fill="none" stroke="var(--paper)" stroke-width="1.3"/>
      <text class="text contact" x="550" y="395">www.qboost480.com</text>
      <!-- pin -->
      <path fill="var(--paper)" d="M534,432 Q526,422 526,417 A8,8 0 1 1 542,417 Q542,422 534,432 Z"/>
      <circle cx="534" cy="417" r="3" fill="var(--mint)"/>
      <text class="text contact" x="550" y="427">2914 Ravensby Street</text>
      <text class="text contact" x="550" y="459">J7T-2K8 Montreal, Quebec</text>
    </svg>
  </section>

  <section class="card card--back" aria-label="Card back">
    <svg viewBox="0 0 1050 600" xmlns="http://www.w3.org/2000/svg">
      <text class="brand" x="80" y="318">Qboost480</text>

      <rect class="band-blue" fill="var(--sky)" x="0" y="340" width="1050" height="22"/>

      <!-- pillars -->
      <text class="pillar" x="650" y="205">SYNC</text>
      <text class="pillar" x="736" y="205">|</text>
      <text class="pillar" x="760" y="205">SHIP</text>
      <text class="pillar" x="834" y="205">|</text>
      <text class="pillar" x="857" y="205">SELL</text>

      <!-- sync icon: computer -->
      <g fill="none" stroke="var(--lime)" stroke-width="3">
        <rect x="652" y="232" width="38" height="25"/>
        <path d="M671,257 L671,265 M661,266 L681,266"/>
        <rect x="692" y="238" width="12" height="30"/>
      </g>
      <!-- ship icon: truck -->
      <g fill="var(--lime)">
        <rect x="752" y="226" width="50" height="34"/>
        <path d="M804,238 L818,238 L826,250 L826,262 L804,262 Z"/>
        <circle cx="765" cy="264" r="7" stroke="var(--paper)" stroke-width="3"/>
        <circle cx="813" cy="264" r="7" stroke="var(--paper)" stroke-width="3"/>
      </g>
      <!-- sell icon: coin -->
      <circle cx="880" cy="245" r="17" fill="none" stroke="var(--lime)" stroke-width="3"/>
      <text x="880" y="254" text-anchor="middle" font-family="Arimo, Arial, sans-serif" font-weight="700" font-size="24" fill="var(--lime)">$</text>

      <text class="tagline" x="612" y="400">Multi Channel Selling</text>
    </svg>
  </section>

</main>
</body>
</html>
```